Brightvane Group Word Press Website

We need a graphical, fun website that conveys our messaging of providing the Top-Tier Keystone Outreach Program for Mortgage Loan Officers and Realtors. Our system uses AI and Predictive Analysis to uncover the 'Gold' hidden in contact databases. The 'Gold' is defined as people who are in the market or likely to be in the market soon. We place that 'Gold' in the form of Contact Name, Address, Phone and Email on a Daily To Do List detailing what type of contact should be made.

Target Market(s)

Mortgage Loan Officers and Realtors

Industry/Entity Type

Mortgage & Real Estate

Coding

Coded - Design and coding required

Number of Pages Required

5+ page

Requirements
Must have
• I like the look of this site- https://www.hearthloanstudio.example/
Nice to have
• Please create a flow that is similar to https://www.hearthloanstudio.example/, but better, more dynamic. Site must be responsive and mobile friendly. Site will have embedded videos. Site need to convey a message of hope, imagination, innovation, results oriented, better than the rest, victory!
Should not have
• Nothing cheesy or low class.

```html
<!DOCTYPE html>
<html lang="en">
<head>
<meta charset="utf-8">
<title>Brightvane Group – Home Loans</title>
<link rel="stylesheet" href="https://fonts.googleapis.com/css2?family=Montserrat:wght@400;500;600;700&display=swap">
<style>
:root{
  --blue:#1489ea;
  --ink:#111;
  --text:#555;
  --muted:#777;
  --panel:#4d4d4d;
  --soft:#f2f2f2;
  --field:#fff;
  --white:#fff;
}
*{box-sizing:border-box;margin:0;padding:0}
html,body{width:1200px;height:4181px;overflow:hidden}
body{font-family:"Montserrat",sans-serif;color:var(--text);background:var(--white);position:relative}
.abs{position:absolute}
/* hero */
.hero{left:0;top:0;width:1200px;height:653px;background:linear-gradient(160deg,#4a5a7a 0%,#2c3650 40%,#1d2434 70%,#2a3a3a 100%)}
.brand{left:110px;top:22px;display:flex;align-items:center;gap:8px;color:var(--white);font-weight:700;font-size:16px;letter-spacing:.3px}
.brand-dot{width:12px;height:12px;background:var(--white)}
.nav{left:606px;top:34px;display:flex;gap:30px;color:var(--white);font-size:14px;font-weight:500}
.signup{left:1000px;top:29px;width:87px;height:30px;background:var(--blue);color:var(--white);font-size:10px;font-weight:600;display:flex;align-items:center;justify-content:center;border-radius:2px}
.hero-title{left:112px;top:205px;font-size:45px;line-height:53px;font-weight:700;color:var(--white)}
.hero-copy{left:112px;top:330px;width:410px;font-size:13.5px;line-height:35px;color:var(--white);font-weight:500}
.hbtn{top:481px;height:42px;background:var(--white);color:#333;font-size:13px;display:flex;align-items:center;justify-content:center;border-radius:2px}
.dots{left:578px;top:622px;display:flex;gap:4px}
.dots span{width:11px;height:11px;border-radius:50%;background:var(--white)}
.dots span.on{background:var(--blue)}
/* about */
.about{left:112px;top:698px;width:364px;height:707px;background:var(--panel);padding:36px 28px;color:#eee}
.about h2{font-size:28px;font-weight:500;color:var(--white);margin-bottom:6px}
.about p{font-size:14.5px;line-height:35px}
.btn-white{left:140px;top:1320px;width:130px;height:42px;background:var(--white);color:var(--blue);font-size:15px;display:flex;align-items:center;justify-content:center;border-radius:2px}
.video{left:503px;top:698px;width:584px;height:434px;background:linear-gradient(180deg,#8c8aa8 0%,#b39a7a 45%,#7a6a58 70%,#6c8ca0 100%)}
.soft{left:502px;top:1155px;font-size:29px;font-weight:600;color:var(--ink)}
.awesome{left:500px;top:1191px;font-size:30px;font-weight:700;color:var(--blue)}
.soft-copy{left:503px;top:1233px;width:585px;font-size:14.5px;line-height:35px;height:170px;overflow:hidden}
/* headings */
.sec-title{left:0;width:1200px;text-align:center;color:var(--ink);font-weight:700}
.sec-sub{left:0;width:1200px;text-align:center;font-size:17px;line-height:26px;color:var(--text)}
/* services */
.card{width:395px;height:193px;background:var(--white);box-shadow:0 2px 10px rgba(0,0,0,.13)}
.card-icon{position:absolute;left:17px;top:20px;width:52px;height:52px;background:#f0f0f0;display:flex;align-items:center;justify-content:center}
.card h3{position:absolute;left:89px;top:31px;font-size:18.5px;font-weight:600;color:var(--ink)}
.card p{position:absolute;left:90px;top:63px;width:290px;font-size:15px;line-height:26px;color:var(--muted)}
.card-foot{position:absolute;left:0;bottom:0;width:100%;height:62px;background:var(--soft);display:flex;align-items:center;justify-content:space-between;padding:0 26px;font-size:17px;color:#444;font-weight:500}
.card-foot.active{background:var(--blue);color:var(--white)}
.plus{font-size:28px;font-weight:400;line-height:1}
/* blog */
.banner{left:0;top:2415px;width:1200px;height:351px;background:linear-gradient(180deg,#4a3f38 0%,#2b3236 55%,#3a4a52 80%,#252a2e 100%)}
.banner h2{position:absolute;top:100px;width:1200px;text-align:center;font-size:36px;font-weight:600;color:var(--white)}
.banner p{position:absolute;left:286px;top:152px;width:628px;text-align:center;font-size:17px;line-height:26.5px;color:var(--white)}
.post{width:293px;height:371px;background:var(--white);box-shadow:0 2px 8px rgba(0,0,0,.1)}
.post-img{height:205px}
.post-meta{display:flex;justify-content:space-between;padding:16px 14px 0 13px;font-size:16px}
.post-meta b{color:var(--blue);font-weight:500}
.post-meta span{color:var(--ink);font-weight:500}
.post p{padding:4px 14px 0 14px;font-size:15px;line-height:26.5px;color:var(--muted)}
/* contact */
.need{left:110px;top:3421px;font-size:24px;font-weight:600;color:var(--ink)}
.need em{font-style:normal;color:var(--blue)}
.need-copy{left:112px;top:3461px;width:470px;font-size:17px;line-height:35px;text-align:justify;height:140px;overflow:hidden}
.btn-blue{left:112px;top:3628px;width:175px;height:51px;background:var(--blue);color:var(--white);font-size:17px;display:flex;align-items:center;justify-content:center}
.form{left:628px;top:3287px;width:455px;height:528px;background:var(--soft)}
.field{position:absolute;left:22px;width:414px;height:50px;background:var(--field);font-size:11px;color:#444;padding:18px 12px}
.submit{position:absolute;left:22px;top:466px;width:414px;height:37px;background:var(--blue);color:var(--white);font-size:12px;font-weight:600;display:flex;align-items:center;justify-content:center}
/* footer */
.footer{left:0;top:3862px;width:1200px;height:319px;background:var(--soft)}
.foot-brand{left:112px;top:3975px;display:flex;align-items:center;gap:8px;font-size:17px;font-weight:700;color:var(--ink)}
.foot-brand i{width:12px;height:12px;background:var(--ink)}
.foot-copy{left:112px;top:4011px;width:228px;font-size:12px;line-height:35px;text-align:justify}
.ql-title{left:432px;top:3902px;font-size:22px;font-weight:500;color:var(--ink)}
.ql{left:432px;top:3954px;font-size:13px;line-height:34px;color:#333;list-style:none}
.touch{left:752px;top:3900px;font-size:36px;font-weight:700;color:var(--ink)}
.email{left:661px;top:3960px;width:422px;height:22px;border-bottom:1px solid #333;font-size:11px;color:#333;padding-left:12px;padding-top:4px}
.socials{left:760px;top:4009px;display:flex;gap:25px}
.socials span{width:40px;height:40px;border-radius:50%;background:var(--blue)}
.copy{left:112px;top:4153px;font-size:10px;color:#333}
.legal{left:915px;top:4153px;font-size:10px;color:#333;display:flex;gap:28px}
</style>
</head>
<body>

<header>
  <div class="abs hero" role="img" aria-label="Modern glass house at dusk with wet street and trees"></div>
  <div class="abs brand"><i class="brand-dot"></i>Brightvane Group</div>
  <nav class="abs nav"><span>Home</span><span>About</span><span>Service</span><span>Blog</span><span>Contact Us</span></nav>
  <div class="abs signup">Sign Up</div>
  <h1 class="abs hero-title">Your Next Home<br>Loan, Made Easy!</h1>
  <p class="abs hero-copy">Lorem Ipsum is simply dummy text of the printing and typesetting industry. Lorem Ipsum has been the industry's standard dummy text ever since the 1500s, when an unknown printer took a galley of type and scrambled</p>
  <div class="abs hbtn" style="left:112px;width:132px">Home Purchase</div>
  <div class="abs hbtn" style="left:261px;width:132px">Home Refinance</div>
  <div class="abs dots"><span></span><span class="on"></span><span></span></div>
</header>

<section>
  <div class="abs about">
    <h2>About Us</h2>
    <p>In finance, a loan is the lending of money by one or more individuals, organizations, or other entities to other individuals, organizations etc. The recipient (i.e., the borrower) incurs a debt and is usually liable to pay interest on that debt until it is repaid as well as to repay the principal amount borrowed.The document evidencing the debt (e.g., a promissory note) will normally specify, among other things, the principal amount of money borrowed, the interest rate the lender is charging, and the date of repayment. A loan entails the reallocation of the subject as-</p>
  </div>
  <div class="abs btn-white">Learn More</div>
  <div class="abs video" role="img" aria-label="Video cover: stone villa with pool at sunset"></div>
  <svg class="abs" style="left:749px;top:871px" width="90" height="90" viewBox="0 0 90 90"><circle cx="45" cy="45" r="42" fill="none" stroke="#fff" stroke-width="3"/><path d="M36 30 L62 45 L36 60Z" fill="#fff"/></svg>
  <div class="abs soft">Soft &amp; Cozy</div>
  <div class="abs awesome">Estate Awesome</div>
  <p class="abs soft-copy">A mortgage loan is a very common type of loan, used by many individuals to purchase residential or commercial property. The lender, usually a financial institution, is given security – a lien on the title to the property – until the mortgage is paid off in full. In the case of home loans, if the borrower defaults on the loan, the bank would have the legal right to repossess the</p>
</section>

<section>
  <h2 class="abs sec-title" style="top:1438px;font-size:39px">Our Service</h2>
  <p class="abs sec-sub" style="top:1489px">Marketing Can Be Overwhelming. The Good<br>News Is, You Have Options.</p>

  <div class="abs card" style="left:183px;top:1579px">
    <div class="card-icon"><svg width="26" height="26" viewBox="0 0 26 26"><circle cx="13" cy="12" r="6" fill="#1489ea"/><rect x="10" y="18" width="6" height="4" fill="#1489ea"/><g stroke="#1489ea" stroke-width="2"><path d="M13 1v3M3 12h3M20 12h3M5 4l2 2M21 4l-2 2"/></g></svg></div>
    <h3>Brand Design &amp; Strategy</h3>
    <p>Similarly, a loan taken out to buy a car may be secured by the car. The</p>
    <div class="card-foot active">Learn More<span class="plus">+</span></div>
  </div>
  <div class="abs card" style="left:622px;top:1579px">
    <div class="card-icon"><svg width="26" height="26" viewBox="0 0 26 26"><rect x="5" y="2" width="16" height="22" rx="3" fill="#7b6ae6"/><path d="M9 10h8M9 14h8M9 18h6" stroke="#fff" stroke-width="1.6"/></svg></div>
    <h3>Content Marketing</h3>
    <p>Content is King but it can take a lot of work to crank out great original</p>
    <div class="card-foot">Learn More<span class="plus">+</span></div>
  </div>
  <div class="abs card" style="left:183px;top:1816px">
    <div class="card-icon"><svg width="28" height="28" viewBox="0 0 28 28"><circle cx="14" cy="14" r="12" fill="none" stroke="#e8473d" stroke-width="2.4"/><circle cx="14" cy="11" r="4.5" fill="#e8473d"/><path d="M6 22c2-5 14-5 16 0" fill="#e8473d"/></svg></div>
    <h3>Social Media Management</h3>
    <p>Social media is one of the best ways to get your company in front of</p>
    <div class="card-foot">Learn More<span class="plus">+</span></div>
  </div>
  <div class="abs card" style="left:622px;top:1816px">
    <div class="card-icon"><svg width="28" height="28" viewBox="0 0 24 24"><path d="M12 2l3 6.5 7 .8-5.2 4.8 1.4 7L12 17.6 5.8 21.1l1.4-7L2 9.3l7-.8z" fill="#f5c518"/></svg></div>
    <h3>Reputation Management</h3>
    <p>When someone checks you out online what are they going to find?</p>
    <div class="card-foot">Learn More<span class="plus">+</span></div>
  </div>
  <div class="abs card" style="left:183px;top:2053px">
    <div class="card-icon"><svg width="28" height="28" viewBox="0 0 28 28"><circle cx="14" cy="14" r="12" fill="none" stroke="#f07b3f" stroke-width="2.2"/><path d="M14 7v9" stroke="#f07b3f" stroke-width="2.6"/><circle cx="14" cy="20" r="1.6" fill="#f07b3f"/></svg></div>
    <h3>Mortgage Chatbot</h3>
    <p>Use a custom chatbot to generate leads on your website and inside of</p>
    <div class="card-foot">Learn More<span class="plus">+</span></div>
  </div>
  <div class="abs card" style="left:622px;top:2053px">
    <div class="card-icon"><svg width="28" height="28" viewBox="0 0 28 28" fill="none" stroke="#b05ae0" stroke-width="1.8"><circle cx="14" cy="14" r="11"/><ellipse cx="14" cy="14" rx="5" ry="11"/><path d="M3 14h22M5 8h18M5 20h18"/></svg></div>
    <h3>Website Development</h3>
    <p>Your website is your most important digital real estate.&nbsp; What does your</p>
    <div class="card-foot">Learn More<span class="plus">+</span></div>
  </div>
</section>

<section>
  <h2 class="abs sec-title" style="top:2284px;font-size:39px">Blogs</h2>
  <p class="abs sec-sub" style="top:2342px">The emergence and growth of blogs in the late<br>coincided with the advent of web publishing</p>
  <div class="abs banner" role="img" aria-label="Contemporary house with pool and loungers at dusk">
    <h2>Modern Contemporary House</h2>
    <p>Real estate is property consisting of land and the buildings on it, along with its natural resources such as crops, minerals or water; immovable property of this nature; an interest vested in this (also) an item of real property, (more generally) buildings or housing in general.[1][2]</p>
  </div>

  <article class="abs post" style="left:112px;top:2793px">
    <div class="post-img" role="img" aria-label="White two-storey house with wood accents" style="background:linear-gradient(180deg,#cfd8e0,#9aa3a8 60%,#6e7a5a)"></div>
    <div class="post-meta"><b>Mill House</b><span>25 April 2022</span></div>
    <p>Residential real estate may contain either a single family or multifamily structure that is available for occupation or for non-busi-</p>
  </article>
  <article class="abs post" style="left:451px;top:2793px">
    <div class="post-img" role="img" aria-label="Modern glass villa lit at twilight" style="background:linear-gradient(180deg,#6f88a8,#8f8f90 55%,#4a4e52)"></div>
    <div class="post-meta"><b>The Lodge</b><span>28 June 2022</span></div>
    <p>The size of an apartment or house can be described in square feet or meters. In the United States, this includes the area of</p>
  </article>
  <article class="abs post" style="left:791px;top:2793px">
    <div class="post-img" role="img" aria-label="Two-storey suburban house with lawn" style="background:linear-gradient(180deg,#8fb4d8,#b8b2a6 55%,#6f8a4c)"></div>
    <div class="post-meta"><b>The Croft</b><span>26 April 2022</span></div>
    <p>Apartment (American English) or Flat (British English) – An individual unit in a multi-unit building. The boundaries of the apartment</p>
  </article>
</section>

<section>
  <h2 class="abs sec-title" style="top:3200px;font-size:43px">Contact Us</h2>
  <h3 class="abs need">Need Concrete Restoration <em>Fast?</em></h3>
  <p class="abs need-copy">Lorem ipsum dolor sit amet, consectetur adipiscing elit, sed do eiusmod tempor incididunt ut labore et dolore magna aliqua. Quis ipsum suspendisse ultrices gravida. Risus commodo viverra maecenas ac-</p>
  <div class="abs btn-blue">Contact Us</div>
  <form class="abs form">
    <div class="field" style="top:28px">First Name</div>
    <div class="field" style="top:92px">Last Name</div>
    <div class="field" style="top:156px">Email</div>
    <div class="field" style="top:221px">Password</div>
    <div class="field" style="top:284px;height:167px">Message</div>
    <div class="submit">Submit</div>
  </form>
</section>

<footer>
  <div class="abs footer"></div>
  <div class="abs foot-brand"><i></i>Brightvane Group</div>
  <p class="abs foot-copy">Real estate is property consisting of land and the buildings on it, along with its natural resources</p>
  <h4 class="abs ql-title">Quick Links</h4>
  <ul class="abs ql"><li>Home</li><li>About Us</li><li>Service</li><li>Server</li><li>Contact Us</li></ul>
  <h4 class="abs touch">Get in touch!</h4>
  <div class="abs email">Enter your Email</div>
  <svg class="abs" style="left:1058px;top:3964px" width="22" height="14" viewBox="0 0 22 14" fill="none" stroke="#222" stroke-width="1.8"><path d="M1 7h19M14 1l6 6-6 6"/></svg>
  <div class="abs socials" aria-label="Social links"><span></span><span></span><span></span><span></span></div>
  <p class="abs copy">© 2022. All rights reserved by Your Company.</p>
  <div class="abs legal"><span>Privacy Policy</span><span>Terms of Use</span></div>
</footer>

</body>
</html>
```